Larkspur Ridge Management - Business Cards

I need business cards. My current logo was designed by a designer at this site and I very much like and am happy with the results. I would like a business card that is trendy, unique, current yet professional. I deal with high net worth clients daily

Target Market(s)

Out of state investors looking to get into the rental market in Ohio

Industry/Entity Type

Property Management, Consulting

Contact Information for Business Card

Name, Title (Chief Financial Officer) office phone number (555) 817-3094 website address larkridgemgmt.example

Font styles to use
Sans Serif

Colors
0054AA
0677BA
7BADD7
CADEEF
E8F1F8
0094D4
00A9DD
6FCCEA
C7EBF8
E9F6FB
00AB8E
00BBA5
67D7C9
C6EFE9
E9F9F6

```html
<!DOCTYPE html>
<html lang="en">
<head>
<meta charset="utf-8">
<title>Larkspur Ridge Management – Business Cards</title>
<link rel="stylesheet" href="https://fonts.googleapis.com/css2?family=Lato:wght@400;700;900&display=swap">
<style>
  :root {
    --navy: #22355a;
    --red: #c8282e;
    --grey: #5a5a5c;
    --light-grey: #c8c8c8;
    --ink: #2b2b2b;
    --card-edge: #dedede;
    --page: #ffffff;
  }
  * { box-sizing: border-box; margin: 0; padding: 0; }
  html, body {
    width: 1200px; height: 1000px; overflow: hidden;
    background: var(--page);
    font-family: "Lato", sans-serif;
  }
  .card {
    position: absolute; left: 249px; width: 703px; height: 402px;
    border: 1px solid var(--card-edge); border-radius: 22px;
    background: #fff; overflow: hidden;
  }
  .card--front { top: 77px; }
  .card--back { top: 522px; }

  .holder { position: absolute; left: 66px; top: 56px; }
  .holder__name {
    font-weight: 900; font-size: 31px; letter-spacing: 0.5px;
    color: var(--navy); line-height: 1;
  }
  .holder__title {
    margin-top: 6px; font-size: 17px; color: var(--red); line-height: 1;
  }
  .holder__rule {
    width: 42px; height: 3px; background: var(--navy); margin-top: 18px;
  }
  .contact { list-style: none; margin-top: 24px; }
  .contact__item {
    display: flex; align-items: center; gap: 12px;
    font-size: 17px; color: var(--ink); height: 26px;
  }
  .contact__icon { width: 14px; height: 14px; fill: var(--red); flex: none; }

  .brand-decor {
    position: absolute; right: 0; bottom: 0; width: 330px; height: 220px;
    background: linear-gradient(135deg, var(--navy) 0%, var(--navy) 45%, var(--grey) 100%);
    border-top-left-radius: 6px;
  }

  .wordmark {
    position: absolute; inset: 0;
    display: flex; align-items: center; justify-content: center; gap: 16px;
  }
  .wordmark__square { width: 26px; height: 26px; background: var(--red); flex: none; }
  .wordmark__name {
    font-weight: 900; font-size: 34px; line-height: 1.1;
    color: var(--navy); text-transform: uppercase; letter-spacing: 1px;
    max-width: 330px;
  }
</style>
</head>
<body>
  <section class="card card--front">
    <div class="holder">
      <h1 class="holder__name">DANIEL MERCER</h1>
      <p class="holder__title">Chief Financial Officer</p>
      <div class="holder__rule"></div>
      <ul class="contact">
        <li class="contact__item">
          <svg class="contact__icon" viewBox="0 0 24 24"><path d="M6.6 10.8a15.1 15.1 0 0 0 6.6 6.6l2.2-2.2c.3-.3.7-.4 1-.2 1.1.4 2.3.6 3.6.6.6 0 1 .4 1 1V20c0 .6-.4 1-1 1A17 17 0 0 1 3 4c0-.6.4-1 1-1h3.5c.6 0 1 .4 1 1 0 1.3.2 2.5.6 3.6.1.3 0 .7-.2 1z"/></svg>
          <span>(555) 817-3094</span>
        </li>
        <li class="contact__item">
          <svg class="contact__icon" viewBox="0 0 24 24"><path d="M2 5h20v14H2z M2 5l10 8 10-8" fill="none" stroke="#c8282e" stroke-width="0"/><path d="M2 5h20L12 12.5z"/><path d="M2 7.2l10 7.6 10-7.6V19H2z"/></svg>
          <span>info@larkridgemgmt.example</span>
        </li>
        <li class="contact__item">
          <svg class="contact__icon" viewBox="0 0 24 24"><circle cx="12" cy="12" r="10"/><path d="M2 12h20M12 2c3 3 3 17 0 20M12 2c-3 3-3 17 0 20" fill="none" stroke="#fff" stroke-width="1.5"/></svg>
          <span>larkridgemgmt.example</span>
        </li>
      </ul>
    </div>
    <div class="brand-decor" role="img" aria-label="Large brand mark decoration area"></div>
  </section>

  <section class="card card--back">
    <div class="wordmark">
      <span class="wordmark__square"></span>
      <span class="wordmark__name">Larkspur Ridge Management</span>
    </div>
  </section>
</body>
</html>
```